Looking for something sharp classy and with an edge for an advanced civil construction business
Something that says professional
nothing too DARK

Target Market(s)

mining companies council civil contractors concrete works

Industry/Entity Type

Construction

Contact Information for Business Card

Brindle Civil Constructions
brindlecivilconstruction@quokkamail.com
Tavi Marlowe
0418275936

Font styles to use
Serif
Sans Serif

Colors
0455a3
0592cd
85cae6
000000
919191

Requirements
Must have
• On the back of the card must have
down the bottom small print email logo phone number

Should not have
• follow us on facebook
Brindle Civil Constructions

follow us on instagram
BRINDLECIVILCONSTRUCTIONS

```html
<!DOCTYPE html>
<html lang="en">
<head>
<meta charset="utf-8">
<title>Brindle Civil Constructions — Business Card</title>
<link rel="stylesheet" href="https://fonts.googleapis.com/css2?family=Caladea:ital,wght@0,400;0,700;1,400&display=swap">
<style>
  :root {
    --stage: #e4e4e4;
    --front-light: #12acd9;
    --front-dark: #0592cd;
    --back: #0455a3;
    --back-dark: #034c93;
    --ink: #ffffff;
    --serif: "Caladea", Cambria, Georgia, serif;
  }
  * { box-sizing: border-box; margin: 0; padding: 0; }
  html, body {
    width: 1200px; height: 864px; overflow: hidden;
    background: var(--stage);
    font-family: var(--serif);
    color: var(--ink);
  }
  .stage {
    position: relative; width: 1200px; height: 864px;
    display: flex; align-items: center; justify-content: center; gap: 44px;
  }
  .card {
    position: relative; width: 540px; height: 330px;
    box-shadow: 0 6px 18px rgba(0,0,0,.18);
  }
  .card-front {
    background: radial-gradient(circle at 38% 35%, var(--front-light), var(--front-dark) 85%);
  }
  .card-back {
    background: linear-gradient(160deg, var(--back), var(--back-dark));
    display: flex; flex-direction: column; align-items: center; justify-content: center;
  }
  .holder { position: absolute; left: 34px; top: 30px; }
  .holder-name { font-weight: 700; font-size: 19px; letter-spacing: .5px; line-height: 1.1; }
  .holder-role { font-weight: 700; font-style: italic; font-size: 18px; line-height: 1.1; }

  .brand-block { position: absolute; right: 30px; bottom: 28px; width: 330px; }
  .brand-name {
    font-weight: 700; font-size: 64px; line-height: .9; letter-spacing: 1px;
    text-align: right; padding-right: 6px;
  }
  .brand-tagline { font-size: 28px; line-height: 1.1; margin-top: 2px; letter-spacing: .3px; }
  .brand-rule { height: 2px; background: var(--ink); margin: 6px 0 8px; }
  .contact { font-size: 16px; line-height: 1.15; }
  .contact-phone { display: flex; align-items: center; gap: 6px; }
  .contact-phone svg { width: 12px; height: 12px; }

  .back-brand { font-weight: 700; font-size: 26px; letter-spacing: 1px; line-height: 1; }
  .back-contact { font-size: 12px; text-align: center; line-height: 1.25; margin-top: 10px; }
</style>
</head>
<body>
<main class="stage">
  <section class="card card-front" aria-label="Business card front">
    <div class="holder">
      <p class="holder-name">TAVI MARLOWE</p>
      <p class="holder-role">Director</p>
    </div>
    <div class="brand-block">
      <p class="brand-name">BRINDLE</p>
      <p class="brand-tagline">Civil Constructions</p>
      <div class="brand-rule"></div>
      <p class="contact contact-phone">
        <svg viewBox="0 0 12 12" aria-hidden="true"><circle cx="6" cy="3.2" r="2.6" fill="#fff"/><path d="M1 12c0-3 2.2-5 5-5s5 2 5 5z" fill="#fff"/></svg>
        0418275936
      </p>
      <p class="contact">brindlecivilconstruction@quokkamail.com</p>
    </div>
  </section>

  <section class="card card-back" aria-label="Business card back">
    <p class="back-brand">BRINDLE</p>
    <div class="back-contact">
      <p>0418275936</p>
      <p>brindlecivilconstruction@quokkamail.com</p>
    </div>
  </section>
</main>
</body>
</html>
```